plumbing & gas fitting business card design

We need a business card design for a plumbing & gas fitting company. The company covers commercial, domestic and maintenance work. We would like a modern design communicating efficiency and sophistication. preferred colours would include (red grey & black) or (green grey & black). Please DO NOT include any water droplets.

Industry/Entity Type

Business

Contact Information for Business Card

Vortig Plumbing & Gas, Commercial Domestic & Maintenance, licence no. 617394K, ABN 47215830962, Phone 0417382956, Email vortigplumbingandgas@corvanet.com

```html
<!DOCTYPE html>
<html lang="en">
<head>
<meta charset="utf-8">
<title>Vortig Plumbing &amp; Gas – Business Card</title>
<link rel="stylesheet" href="https://fonts.googleapis.com/css2?family=Arimo:wght@400;700&display=swap">
<style>
  :root {
    --page-bg: #e9eaec;
    --card-white: #f2f2f3;
    --marble-grey: #c9cbce;
    --brand-red: #8e2f27;
    --brand-red-dark: #5e1d18;
    --brand-red-light: #a8453b;
    --ink: #111111;
    --name-ink: #f1ece8;
    --leather: #6b3a22;
    --leather-dark: #3a2217;
    --skin: #c98f6b;
  }
  * { margin: 0; padding: 0; box-sizing: border-box; }
  html, body {
    width: 1200px; height: 705px; overflow: hidden;
    background: var(--page-bg);
    font-family: "Arimo", Arial, sans-serif;
  }
  .card {
    position: absolute; left: 90px; top: 62px;
    width: 1020px; height: 582px;
    background: linear-gradient(160deg, var(--card-white) 0%, var(--marble-grey) 100%);
    overflow: hidden;
    box-shadow: 0 10px 30px rgba(0,0,0,.25);
  }
  .red-band {
    position: absolute; left: 0; top: 0; width: 100%; height: 262px;
    background: linear-gradient(135deg, var(--brand-red-light) 0%, var(--brand-red) 45%, var(--brand-red-dark) 100%);
  }
  .work-photo {
    position: absolute; left: 0; top: 0; width: 330px; height: 100%;
    background: linear-gradient(180deg, var(--skin) 0%, var(--leather) 45%, var(--leather-dark) 100%);
  }
  .fitting-photo {
    position: absolute; left: 330px; top: 262px; right: 0; bottom: 0;
    background: linear-gradient(120deg, rgba(180,130,110,.35) 0%, rgba(200,200,205,.15) 60%, rgba(150,150,155,.3) 100%);
  }
  .brand-name {
    position: absolute; right: 70px; top: 62px;
    font-weight: 700; font-size: 54px; letter-spacing: 1px;
    color: var(--name-ink); text-transform: uppercase;
    text-align: right; line-height: 1.1;
  }
  .tagline {
    position: absolute; right: 70px; top: 205px;
    font-weight: 700; font-size: 26px; color: var(--ink);
  }
  .credentials {
    position: absolute; left: 360px; right: 50px; top: 292px;
    display: flex; justify-content: space-between;
    font-weight: 700; font-size: 30px; color: var(--ink);
  }
  .phone {
    position: absolute; right: 50px; top: 390px;
    display: flex; align-items: center; gap: 14px;
    font-weight: 700; font-size: 66px; color: var(--ink); letter-spacing: 1px;
  }
  .email {
    position: absolute; right: 50px; top: 490px;
    display: flex; align-items: center; gap: 12px;
    font-weight: 700; font-size: 30px; color: var(--ink);
  }
  .icon { display: block; }
</style>
</head>
<body>
  <main class="card">
    <div class="red-band"></div>
    <div class="fitting-photo" role="img" aria-label="Faded photo of copper pipe fittings over a bathroom plan"></div>
    <div class="work-photo" role="img" aria-label="Photo of a plumber's gloved hand with a pipe wrench in a leather tool belt"></div>

    <h1 class="brand-name">Vortig<br>Plumbing &amp; Gas</h1>
    <p class="tagline">Commercial Domestic &amp; Maintenance</p>

    <div class="credentials">
      <span class="licence">licence 617394K</span>
      <span class="abn">abn 47215830962</span>
    </div>

    <div class="phone">
      <svg class="icon" width="40" height="48" viewBox="0 0 24 24" aria-hidden="true">
        <path fill="#111" d="M6.6 10.8a15.1 15.1 0 0 0 6.6 6.6l2.2-2.2a1 1 0 0 1 1-.25 11.4 11.4 0 0 0 3.6.57 1 1 0 0 1 1 1V20a1 1 0 0 1-1 1A17 17 0 0 1 3 4a1 1 0 0 1 1-1h3.5a1 1 0 0 1 1 1c0 1.25.2 2.45.57 3.57a1 1 0 0 1-.25 1z"/>
      </svg>
      <span>0417382956</span>
    </div>

    <div class="email">
      <svg class="icon" width="30" height="30" viewBox="0 0 24 24" aria-hidden="true">
        <path fill="none" stroke="#111" stroke-width="2.4" d="M20 13v7H4V4h7"/>
        <path fill="#111" d="M9 15l1-4 9-9 3 3-9 9z"/>
      </svg>
      <span>vortigplumbingandgas@corvanet.com</span>
    </div>
  </main>
</body>
</html>
```